Etiketten für Honig
Zielgruppe
Es scheint Missverständnisse zu geben weshalb ich das Briefing wohl ändern muss.
see below for English translation
Wir sind eine kleine Imkerei, die von der Liebhaberei in den Nebenerwerb wechselt. Wir verkaufen verschiedene Sortenhonige und Honigzubereitungen (siehe Webseite) im vorwiegend ländlichen Raum des Münsterlandes.
Entsprechend unseres Standortes und unserer Kundschaft benötigen wir ein klassisch ländliches Design. Hierfür haben wir auch bereits ein Logo welches verwendet werden muss.
English
There seems to be some misunderstanding, so I guess I'll have to change the briefing.
We are a small apiary that changes from hobby to sideline. We sell different types of honey and honey preparations (e.g. honey with raspberry) in a predominantly rural area of the Münsterland (Muensterland).
According to our location and our clientele, we need a classic rural design. We already have a logo which must be used.
Aufgabenstellung
Wir möchten ein rechteckiges Etikett mit Gewährverschluss das für verschiedene Sorten adoptierbar ist. Zum Beispiel durch den Austausch der Sortenbezeichnung und eine farbliche Veränderung.
Das Design soll später auf Naturpapier oder Graspapier gedruckt werden. Das Logo muss auf Etikett und Gewährverschluss abgebildet werden.
We would like a rectangular label with a guarantee seal that is adoptable for different varieties. For example, by exchanging the variety designation and changing the color.
The design will later be printed on uncoated paper or grass paper. The logo must be shown on the label and guarantee seal.

```html
<!DOCTYPE html>
<html lang="de">
<head>
<meta charset="utf-8">
<title>Honigmanufaktur Lindhorst – Etiketten mit Gewährverschluss</title>
<link rel="stylesheet" href="https://fonts.googleapis.com/css2?family=Kaushan+Script&family=Source+Sans+3:wght@400;600&display=swap">
<style>
  :root {
    --canvas: #ffffff;
    --paper: #e3dfd5;
    --ink: #6b6760;
    --mark: #e9b533;
    --cream: #ffffff;
  }
  * { box-sizing: border-box; margin: 0; padding: 0; }
  html, body { width: 1200px; height: 2383px; overflow: hidden; background: var(--canvas); }
  .sheet {
    position: relative; width: 1200px; height: 2383px;
    display: grid; grid-template-columns: repeat(3, 385px); grid-template-rows: repeat(3, 752px);
    padding-left: 33.5px;
  }
  .variant { position: relative; width: 385px; height: 752px; }

  .v1 { --light: #fce4df; --dark: #8e3f37; --mid: #e89a8e; }
  .v2 { --light: #ebe4f0; --dark: #6a4672; --mid: #b58fc3; }
  .v3 { --light: #dbe8ee; --dark: #2a535a; --mid: #7fb3cc; }
  .v4 { --light: #cde6f7; --dark: #035269; --mid: #5ab8e0; }
  .v5 { --light: #fde9cb; --dark: #6e533b; --mid: #d9b48e; }
  .v6 { --light: #e0ecc9; --dark: #3f6427; --mid: #9cc25a; }
  .v7 { --light: #fdeec6; --dark: #7c5919; --mid: #f2c040; }
  .v8 { --light: #d6eadb; --dark: #305c3b; --mid: #7dbf98; }
  .v9 { --light: #f1ed98; --dark: #5c5b1f; --mid: #c6c84c; }

  /* guarantee seal */
  .seal-strip {
    position: absolute; left: 165px; top: 240px; width: 55px; height: 272px;
    background: var(--dark); z-index: 2;
  }
  .seal {
    position: absolute; left: 114px; top: 161px; width: 157px; height: 157px;
    border-radius: 50%; background: var(--light); z-index: 3; text-align: center;
  }
  .seal .mark { top: 30px; width: 40px; height: 40px; }
  .seal .brand { top: 78px; font-size: 24px; }

  /* label */
  .label {
    position: absolute; left: 51.5px; top: 503px; width: 282px; height: 235px;
    z-index: 1; text-align: center;
  }
  .label-bands { position: absolute; inset: 0; display: block; }
  .paper { fill: var(--paper); }
  .band-light { fill: var(--light); }
  .band-top { fill: var(--mid); }
  .band-dark { fill: var(--dark); }
  .meadow { fill: var(--mid); }

  .mark {
    position: absolute; left: 50%; transform: translateX(-50%);
    border-radius: 50%; background: var(--mark);
  }
  .label .mark { top: 24px; width: 56px; height: 56px; }
  .brand {
    position: absolute; left: 0; right: 0;
    font-family: "Source Sans 3", sans-serif; font-weight: 600; color: var(--ink);
    line-height: 1;
  }
  .label .brand { top: 88px; font-size: 30px; }
  .origin {
    position: absolute; left: 0; right: 0; top: 122px;
    font-family: "Source Sans 3", sans-serif; font-weight: 400; font-size: 14px; color: var(--ink);
  }
  .tagline {
    position: absolute; left: 0; right: 0; top: 160px;
    font-family: "Kaushan Script", cursive; font-size: 12px; color: var(--cream);
  }
  .variety {
    position: absolute; left: 0; right: 0; top: 192px;
    font-family: "Kaushan Script", cursive; font-size: 19px; color: var(--cream);
  }
</style>
</head>
<body>
<main class="sheet">

  <section class="variant v1">
    <div class="seal"><span class="mark"></span><span class="brand">Lindhorst</span></div>
    <div class="seal-strip"></div>
    <div class="label">
      <svg class="label-bands" viewBox="0 0 282 235" width="282" height="235">
        <rect class="paper" width="282" height="235"/>
        <path class="band-top" d="M0 0H282V8C230 12 190 4 140 8S40 14 0 6Z"/>
        <path class="band-light" d="M0 6C40 14 100 4 140 8S230 12 282 8V16C230 22 190 10 140 16S40 24 0 14Z"/>
        <path class="band-dark" d="M0 146C60 138 120 152 180 144S260 140 282 146V235H0Z"/>
        <path class="meadow" role="img" aria-label="Blumenwiese als Muster" d="M0 194C70 186 140 198 210 190S270 188 282 192V235H0Z"/>
      </svg>
      <span class="mark"></span><span class="brand">Lindhorst</span>
      <span class="origin">Auenhonig</span>
      <span class="tagline">Honig aus dem Münsterland</span>
      <span class="variety">Akazienhonig</span>
    </div>
  </section>

  <section class="variant v2">
    <div class="seal"><span class="mark"></span><span class="brand">Lindhorst</span></div>
    <div class="seal-strip"></div>
    <div class="label">
      <svg class="label-bands" viewBox="0 0 282 235" width="282" height="235">
        <rect class="paper" width="282" height="235"/>
        <path class="band-top" d="M0 0H282V8C230 12 190 4 140 8S40 14 0 6Z"/>
        <path class="band-light" d="M0 6C40 14 100 4 140 8S230 12 282 8V16C230 22 190 10 140 16S40 24 0 14Z"/>
        <path class="band-dark" d="M0 146C60 138 120 152 180 144S260 140 282 146V235H0Z"/>
        <path class="meadow" role="img" aria-label="Blumenwiese als Muster" d="M0 194C70 186 140 198 210 190S270 188 282 192V235H0Z"/>
      </svg>
      <span class="mark"></span><span class="brand">Lindhorst</span>
      <span class="origin">Auenhonig</span>
      <span class="tagline">Honig aus dem Münsterland</span>
      <span class="variety">Akazienhonig</span>
    </div>
  </section>

  <section class="variant v3">
    <div class="seal"><span class="mark"></span><span class="brand">Lindhorst</span></div>
    <div class="seal-strip"></div>
    <div class="label">
      <svg class="label-bands" viewBox="0 0 282 235" width="282" height="235">
        <rect class="paper" width="282" height="235"/>
        <path class="band-top" d="M0 0H282V8C230 12 190 4 140 8S40 14 0 6Z"/>
        <path class="band-light" d="M0 6C40 14 100 4 140 8S230 12 282 8V16C230 22 190 10 140 16S40 24 0 14Z"/>
        <path class="band-dark" d="M0 146C60 138 120 152 180 144S260 140 282 146V235H0Z"/>
        <path class="meadow" role="img" aria-label="Blumenwiese als Muster" d="M0 194C70 186 140 198 210 190S270 188 282 192V235H0Z"/>
      </svg>
      <span class="mark"></span><span class="brand">Lindhorst</span>
      <span class="origin">Auenhonig</span>
      <span class="tagline">Honig aus dem Münsterland</span>
      <span class="variety">Frühtracht</span>
    </div>
  </section>

  <section class="variant v4">
    <div class="seal"><span class="mark"></span><span class="brand">Lindhorst</span></div>
    <div class="seal-strip"></div>
    <div class="label">
      <svg class="label-bands" viewBox="0 0 282 235" width="282" height="235">
        <rect class="paper" width="282" height="235"/>
        <path class="band-top" d="M0 0H282V8C230 12 190 4 140 8S40 14 0 6Z"/>
        <path class="band-light" d="M0 6C40 14 100 4 140 8S230 12 282 8V16C230 22 190 10 140 16S40 24 0 14Z"/>
        <path class="band-dark" d="M0 146C60 138 120 152 180 144S260 140 282 146V235H0Z"/>
        <path class="meadow" role="img" aria-label="Blumenwiese als Muster" d="M0 194C70 186 140 198 210 190S270 188 282 192V235H0Z"/>
      </svg>
      <span class="mark"></span><span class="brand">Lindhorst</span>
      <span class="origin">Auenhonig</span>
      <span class="tagline">Honig aus dem Münsterland</span>
      <span class="variety">Akazienhonig</span>
    </div>
  </section>

  <section class="variant v5">
    <div class="seal"><span class="mark"></span><span class="brand">Lindhorst</span></div>
    <div class="seal-strip"></div>
    <div class="label">
      <svg class="label-bands" viewBox="0 0 282 235" width="282" height="235">
        <rect class="paper" width="282" height="235"/>
        <path class="band-top" d="M0 0H282V8C230 12 190 4 140 8S40 14 0 6Z"/>
        <path class="band-light" d="M0 6C40 14 100 4 140 8S230 12 282 8V16C230 22 190 10 140 16S40 24 0 14Z"/>
        <path class="band-dark" d="M0 146C60 138 120 152 180 144S260 140 282 146V235H0Z"/>
        <path class="meadow" role="img" aria-label="Blumenwiese als Muster" d="M0 194C70 186 140 198 210 190S270 188 282 192V235H0Z"/>
      </svg>
      <span class="mark"></span><span class="brand">Lindhorst</span>
      <span class="origin">Auenhonig</span>
      <span class="tagline">Honig aus dem Münsterland</span>
      <span class="variety">Akazienhonig</span>
    </div>
  </section>

  <section class="variant v6">
    <div class="seal"><span class="mark"></span><span class="brand">Lindhorst</span></div>
    <div class="seal-strip"></div>
    <div class="label">
      <svg class="label-bands" viewBox="0 0 282 235" width="282" height="235">
        <rect class="paper" width="282" height="235"/>
        <path class="band-top" d="M0 0H282V8C230 12 190 4 140 8S40 14 0 6Z"/>
        <path class="band-light" d="M0 6C40 14 100 4 140 8S230 12 282 8V16C230 22 190 10 140 16S40 24 0 14Z"/>
        <path class="band-dark" d="M0 146C60 138 120 152 180 144S260 140 282 146V235H0Z"/>
        <path class="meadow" role="img" aria-label="Blumenwiese als Muster" d="M0 194C70 186 140 198 210 190S270 188 282 192V235H0Z"/>
      </svg>
      <span class="mark"></span><span class="brand">Lindhorst</span>
      <span class="origin">Auenhonig</span>
      <span class="tagline">Honig aus dem Münsterland</span>
      <span class="variety">Akazienhonig</span>
    </div>
  </section>

  <section class="variant v7">
    <div class="seal"><span class="mark"></span><span class="brand">Lindhorst</span></div>
    <div class="seal-strip"></div>
    <div class="label">
      <svg class="label-bands" viewBox="0 0 282 235" width="282" height="235">
        <rect class="paper" width="282" height="235"/>
        <path class="band-top" d="M0 0H282V8C230 12 190 4 140 8S40 14 0 6Z"/>
        <path class="band-light" d="M0 6C40 14 100 4 140 8S230 12 282 8V16C230 22 190 10 140 16S40 24 0 14Z"/>
        <path class="band-dark" d="M0 146C60 138 120 152 180 144S260 140 282 146V235H0Z"/>
        <path class="meadow" role="img" aria-label="Blumenwiese als Muster" d="M0 194C70 186 140 198 210 190S270 188 282 192V235H0Z"/>
      </svg>
      <span class="mark"></span><span class="brand">Lindhorst</span>
      <span class="origin">Auenhonig</span>
      <span class="tagline">Honig aus dem Münsterland</span>
      <span class="variety">Akazienhonig</span>
    </div>
  </section>

  <section class="variant v8">
    <div class="seal"><span class="mark"></span><span class="brand">Lindhorst</span></div>
    <div class="seal-strip"></div>
    <div class="label">
      <svg class="label-bands" viewBox="0 0 282 235" width="282" height="235">
        <rect class="paper" width="282" height="235"/>
        <path class="band-top" d="M0 0H282V8C230 12 190 4 140 8S40 14 0 6Z"/>
        <path class="band-light" d="M0 6C40 14 100 4 140 8S230 12 282 8V16C230 22 190 10 140 16S40 24 0 14Z"/>
        <path class="band-dark" d="M0 146C60 138 120 152 180 144S260 140 282 146V235H0Z"/>
        <path class="meadow" role="img" aria-label="Blumenwiese als Muster" d="M0 194C70 186 140 198 210 190S270 188 282 192V235H0Z"/>
      </svg>
      <span class="mark"></span><span class="brand">Lindhorst</span>
      <span class="origin">Auenhonig</span>
      <span class="tagline">Honig aus dem Münsterland</span>
      <span class="variety">Akazienhonig</span>
    </div>
  </section>

  <section class="variant v9">
    <div class="seal"><span class="mark"></span><span class="brand">Lindhorst</span></div>
    <div class="seal-strip"></div>
    <div class="label">
      <svg class="label-bands" viewBox="0 0 282 235" width="282" height="235">
        <rect class="paper" width="282" height="235"/>
        <path class="band-top" d="M0 0H282V8C230 12 190 4 140 8S40 14 0 6Z"/>
        <path class="band-light" d="M0 6C40 14 100 4 140 8S230 12 282 8V16C230 22 190 10 140 16S40 24 0 14Z"/>
        <path class="band-dark" d="M0 146C60 138 120 152 180 144S260 140 282 146V235H0Z"/>
        <path class="meadow" role="img" aria-label="Blumenwiese als Muster" d="M0 194C70 186 140 198 210 190S270 188 282 192V235H0Z"/>
      </svg>
      <span class="mark"></span><span class="brand">Lindhorst</span>
      <span class="origin">Auenhonig</span>
      <span class="tagline">Honig aus dem Münsterland</span>
      <span class="variety">Akazienhonig</span>
    </div>
  </section>

</main>
</body>
</html>
```